New Graphic Design Project

I need the following
2 versions (CMYK and RGB)
Full Page ad design 7.5" wide x 10" tall
No less than 300 dpi for print and 72dpi for web:
Full Color CMYK for print and RGB for web
Provide a high quality JPEG of the ad as well.

You can use the attached post card as a guide and use the info within it. You can get more information from our website at HaulBrightCrew.com.
Also add a block with the following ... We work with real estate agents to make moving stress - free for their clients:
*Old Fashioned Customer Service
*Discounted rates
*Always Free Estimates
*Fully Licensed and Insured
*Communication From Start To Finish
*Full Service Moving

```html
<!DOCTYPE html>
<html lang="en">
<head>
<meta charset="utf-8">
<title>HaulBright Crew – Real Estate Agent Ad</title>
<link rel="stylesheet" href="https://fonts.googleapis.com/css2?family=Lexend:wght@400;600;800&family=Kaushan+Script&display=swap">
<style>
  :root {
    --orange: #f4a052;
    --dark: #2e2f2f;
    --ink: #262626;
    --white: #ffffff;
    --stage: #ececec;
  }
  * { margin: 0; padding: 0; box-sizing: border-box; }
  html, body { width: 1068px; height: 1200px; overflow: hidden; background: var(--stage); }
  .ad {
    position: absolute; left: 84px; top: 0;
    width: 900px; height: 1200px;
    background: var(--white);
    overflow: hidden;
    font-family: "Lexend", sans-serif;
  }
  .ad-art { position: absolute; inset: 0; width: 900px; height: 1200px; }
  .headline { font-family: "Lexend", sans-serif; font-weight: 800; }
  .headline--dark { fill: var(--ink); }
  .headline--light { fill: var(--white); }
  .service-item { font-family: "Lexend", sans-serif; font-weight: 400; font-size: 19px; fill: var(--ink); }
  .tagline {
    position: absolute; left: 30px; top: 830px;
    font-family: "Kaushan Script", cursive;
    font-size: 46px; line-height: 52px;
    color: var(--white);
    -webkit-text-stroke: 2px var(--ink);
    paint-order: stroke fill;
    text-shadow: 0 0 3px var(--orange), 2px 2px 0 var(--orange), -2px -2px 0 var(--orange), 2px -2px 0 var(--orange), -2px 2px 0 var(--orange);
    transform: rotate(-5deg);
    transform-origin: left top;
  }
  .tagline span { display: block; }
  .tagline span + span { margin-left: -6px; }
  .brand-name {
    position: absolute; left: 78px; top: 992px; width: 290px;
    font-family: "Lexend", sans-serif; font-weight: 600;
    font-size: 24px; color: var(--white);
    display: flex; align-items: center; justify-content: center; gap: 10px;
  }
  .brand-name::before {
    content: ""; width: 14px; height: 14px; border-radius: 50%; background: var(--white);
  }
  .contact { font-family: "Lexend", sans-serif; font-weight: 400; font-size: 17.5px; }
  .contact--light { fill: var(--white); }
  .contact--accent { fill: var(--orange); }
</style>
</head>
<body>
<main class="ad">
  <svg class="ad-art" viewBox="0 0 900 1200" xmlns="http://www.w3.org/2000/svg">
    <!-- headline bands -->
    <polygon fill="var(--orange)" points="46,0 900,0 900,82 27,82"/>
    <polygon fill="var(--orange)" points="8,157 900,157 900,217 0,217"/>
    <rect fill="var(--dark)" x="0" y="217" width="900" height="983"/>
    <polygon fill="var(--orange)" points="0,335 873,335 857,402 0,402"/>

    <text class="headline headline--dark" x="53" y="72" font-size="74" textLength="572" lengthAdjust="spacingAndGlyphs">WE WORK WITH</text>
    <text class="headline headline--dark" x="53" y="143" font-size="70" textLength="788" lengthAdjust="spacingAndGlyphs">REAL ESTATE AGENTS</text>
    <text class="headline headline--dark" x="57" y="205" font-size="54" textLength="479" lengthAdjust="spacingAndGlyphs">TO MAKE MOVING</text>
    <text class="headline headline--light" x="52" y="315" font-size="110" textLength="795" lengthAdjust="spacingAndGlyphs">STRESS-FREE</text>
    <text class="headline headline--dark" x="53" y="388" font-size="56" textLength="536" lengthAdjust="spacingAndGlyphs">FOR THEIR CLIENTS:</text>

    <!-- services block -->
    <polygon fill="var(--orange)" points="15,430 63,430 15,610"/>
    <polygon fill="var(--white)" points="90,430 104,430 29,667 15,667"/>
    <defs>
      <linearGradient id="movers-tone" x1="0" y1="0" x2="1" y2="1">
        <stop offset="0" stop-color="#c9c4bb"/>
        <stop offset="0.5" stop-color="#8f8372"/>
        <stop offset="1" stop-color="#4a4038"/>
      </linearGradient>
      <linearGradient id="room-tone" x1="0" y1="0" x2="1" y2="1">
        <stop offset="0" stop-color="#e4e0d8"/>
        <stop offset="0.55" stop-color="#a98a66"/>
        <stop offset="1" stop-color="#5b3f2a"/>
      </linearGradient>
      <linearGradient id="truck-tone" x1="0" y1="0" x2="0" y2="1">
        <stop offset="0" stop-color="#8d8680"/>
        <stop offset="0.45" stop-color="#c9c8c6"/>
        <stop offset="0.75" stop-color="#8e6a58"/>
        <stop offset="1" stop-color="#7a4e40"/>
      </linearGradient>
    </defs>
    <g role="img" aria-label="Photo of two movers wheeling blanket-wrapped furniture on a dolly">
      <polygon fill="url(#movers-tone)" points="108,430 233,430 182,667 40,667"/>
    </g>
    <g role="img" aria-label="Photo of a room with packed moving boxes and house plants">
      <polygon fill="url(#room-tone)" points="241,430 432,430 381,667 190,667"/>
    </g>

    <polygon fill="var(--orange)" points="891,470 891,667 845,667"/>
    <polygon fill="var(--white)" points="443,430 889,430 879,463 433,463"/>
    <polygon fill="var(--white)" points="432,470 878,470 868,503 422,503"/>
    <polygon fill="var(--white)" points="421,510 867,510 857,543 411,543"/>
    <polygon fill="var(--white)" points="410,550 856,550 846,583 400,583"/>
    <polygon fill="var(--white)" points="399,590 845,590 835,623 389,623"/>
    <polygon fill="var(--white)" points="388,630 834,630 824,667 378,667"/>
    <text class="service-item" x="480" y="453">Old Fashioned Customer Service</text>
    <text class="service-item" x="468" y="493">Discounted rates</text>
    <text class="service-item" x="453" y="533">Always Free Estimates</text>
    <text class="service-item" x="440" y="573">Fully Licensed and Insured</text>
    <text class="service-item" x="425" y="614">Communication From Start To Finish</text>
    <text class="service-item" x="411" y="654">Full Service Moving</text>

    <!-- truck photo -->
    <g role="img" aria-label="Photo of a white pickup truck towing an enclosed moving trailer outside an apartment building">
      <rect fill="url(#truck-tone)" x="0" y="667" width="900" height="388"/>
    </g>
    <polygon fill="var(--orange)" points="0,688 60,688 0,880"/>
    <polygon fill="var(--white)" points="900,745 900,1000 827,1000"/>

    <!-- brand plate -->
    <polygon fill="var(--white)" points="48,986 56,986 44,1041 36,1041"/>
    <polygon fill="var(--dark)" points="80,974 385,974 367,1041 55,1041"/>
    <polygon fill="var(--orange)" points="393,980 403,980 387,1041 377,1041"/>

    <!-- contact panel -->
    <rect fill="var(--dark)" x="0" y="1055" width="900" height="145"/>
    <polygon fill="var(--white)" points="140,1047 430,1047 428,1055 138,1055"/>
    <polygon fill="var(--orange)" points="486,1047 830,1047 828,1055 484,1055"/>
    <polygon fill="var(--orange)" points="100,1055 130,1055 90,1200 60,1200"/>
    <polygon fill="var(--white)" points="132,1055 160,1055 120,1200 92,1200"/>
    <polygon fill="var(--white)" points="781,1055 806,1055 770,1200 749,1200"/>
    <polygon fill="var(--orange)" points="808,1055 830,1055 792,1200 772,1200"/>

    <g class="contact">
      <circle class="contact--light" cx="176" cy="1083" r="4.5"/>
      <text class="contact contact--light" x="186" y="1090">Address: 4870 Cedar Hollow Ln, Rowlett, TX 75088, United States</text>
      <circle class="contact--light" cx="167" cy="1113" r="4.5"/>
      <text class="contact contact--light" x="177" y="1120">Email: haulbrightcrew1@mailbox.com</text>
      <circle class="contact--accent" cx="158" cy="1142" r="4.5"/>
      <text class="contact contact--accent" x="168" y="1149">Call Us: (972) 555-0147</text>
      <circle class="contact--accent" cx="415" cy="1142" r="4.5"/>
      <text class="contact contact--accent" x="425" y="1149">TxDMV Toll-Free 1-888-555-0192</text>
      <circle class="contact--accent" cx="149" cy="1171" r="4.5"/>
      <text class="contact contact--accent" x="159" y="1178">TxDMV No. 004218856B</text>
      <circle class="contact--accent" cx="399" cy="1171" r="4.5"/>
      <text class="contact contact--accent" x="409" y="1178">USDOT: 3704152</text>
    </g>
  </svg>

  <p class="tagline"><span>Our Backs Are Strong...</span><span>our Reputation Stronger!</span></p>
  <p class="brand-name">HaulBright Crew</p>
</main>
</body>
</html>
```